All Natural Raw Honey & Goats Milk Body Wash Labels

We have launched a new product line of all natural Raw Honey & Goats Milk body wash with the business name being Dawn Meadow and the tag line Naturally . Their are currently three line items requiring three labels. Natural (Unscented), Japanese Honeysuckle and Caribbean.
It is a family orientated product that we want to promote as being all natural, healthy and trustworthy. It is an all Australian made product that uses our very own award winning raw honey
I can supply the file for the business name/logo upon request

Target Market(s)

Families

Industry/Entity Type

Bath & body

Requirements
Must have
• a Lux high end feel
Nice to have
• simple easy to read with minimal images
Should not have
• No cartoons

```html
<!DOCTYPE html>
<html lang="en">
<head>
<meta charset="utf-8">
<title>Dawn Meadow — Raw Honey &amp; Goats Milk Body Wash Labels</title>
<link href="https://fonts.googleapis.com/css2?family=Jost:wght@400;500&family=Oswald:wght@500&display=swap" rel="stylesheet">
<style>
  :root {
    --page: #f6ebe1;
    --ink-light: #ffffff;

    --natural-top: #b4dcb6;
    --natural-mid: #a6d6ac;
    --natural-low: #c3e6c3;
    --natural-band: #e9f4e5;
    --natural-name: #8dbd93;

    --honey-top: #f58025;
    --honey-mid: #f7892c;
    --honey-low: #ff9f33;
    --honey-band: #ffe0a6;
    --honey-name: #ef8426;

    --carib-top: #8fc6c5;
    --carib-mid: #96cccb;
    --carib-low: #a7dcdb;
    --carib-band: #e3f2f0;
    --carib-name: #75aeae;
  }
  * { box-sizing: border-box; margin: 0; padding: 0; }
  html, body {
    width: 1200px;
    height: 900px;
    overflow: hidden;
    background: var(--page);
  }
  .label-set {
    width: 1200px;
    height: 900px;
    display: flex;
    justify-content: center;
    align-items: center;
    gap: 50px;
  }
  .label {
    position: relative;
    width: 320px;
    height: 600px;
    display: flex;
    flex-direction: column;
    font-family: "Jost", "Futura", sans-serif;
    color: var(--ink-light);
    box-shadow: 0 6px 24px rgba(120, 90, 60, 0.12);
  }
  .label__field {
    flex: 0 0 67.5%;
    display: flex;
    flex-direction: column;
    align-items: center;
    padding-top: 178px;
  }
  .label__brand {
    font-size: 30px;
    font-weight: 500;
    letter-spacing: 0.5px;
    margin-bottom: 58px;
  }
  .label__ingredients {
    font-size: 16px;
    font-weight: 500;
    letter-spacing: 0.2px;
  }
  .label__product {
    font-size: 28px;
    font-weight: 500;
    letter-spacing: 0.5px;
    line-height: 1.15;
  }
  .label__variant {
    flex: 0 0 7.5%;
    display: flex;
    align-items: center;
    justify-content: center;
    font-family: "Oswald", "Arial Narrow", sans-serif;
    font-weight: 500;
    font-size: 24px;
    letter-spacing: 0.5px;
    text-transform: uppercase;
  }
  .label__base { flex: 1; }

  .label--natural .label__field { background: linear-gradient(180deg, var(--natural-top), var(--natural-mid) 60%, var(--natural-low)); }
  .label--natural .label__variant { background: var(--natural-band); color: var(--natural-name); }
  .label--natural .label__base { background: linear-gradient(180deg, var(--natural-low), var(--natural-mid)); }

  .label--honeysuckle .label__field { background: linear-gradient(180deg, var(--honey-top), var(--honey-mid) 60%, var(--honey-low)); }
  .label--honeysuckle .label__variant { background: var(--honey-band); color: var(--honey-name); }
  .label--honeysuckle .label__base { background: linear-gradient(180deg, var(--honey-low), var(--honey-top)); }

  .label--caribbean .label__field { background: linear-gradient(180deg, var(--carib-top), var(--carib-mid) 60%, var(--carib-low)); }
  .label--caribbean .label__variant { background: var(--carib-band); color: var(--carib-name); }
  .label--caribbean .label__base { background: linear-gradient(180deg, var(--carib-low), var(--carib-top)); }
</style>
</head>
<body>
  <main class="label-set">
    <article class="label label--natural">
      <div class="label__field">
        <p class="label__brand">Dawn Meadow</p>
        <p class="label__ingredients">Raw Honey &amp; Goats Milk</p>
        <h2 class="label__product">BODY WASH</h2>
      </div>
      <p class="label__variant">Natural (Unscented)</p>
      <div class="label__base"></div>
    </article>

    <article class="label label--honeysuckle">
      <div class="label__field">
        <p class="label__brand">Dawn Meadow</p>
        <p class="label__ingredients">Raw Honey &amp; Goats Milk</p>
        <h2 class="label__product">BODY WASH</h2>
      </div>
      <p class="label__variant">Japanese Honey Suckle</p>
      <div class="label__base"></div>
    </article>

    <article class="label label--caribbean">
      <div class="label__field">
        <p class="label__brand">Dawn Meadow</p>
        <p class="label__ingredients">Raw Honey &amp; Goats Milk</p>
        <h2 class="label__product">BODY WASH</h2>
      </div>
      <p class="label__variant">Caribbean</p>
      <div class="label__base"></div>
    </article>
  </main>
</body>
</html>
```